Rock, Paper Scissors Championship Flyer

We need a dynamic, bold and exciting flyer to promote the following event at our sports center. The event will be primarily focused for adults, but children are welcome to join

Rock, Paper, Scissors Championship - $$$ prizes
Date: June 9th, 2018
Time: 11am-4pm
Fee: $2 to enter, free for spectators
Heats to determine the overall ‘Rock, Paper, Scissors’ champion!
- Cash prizes on offer
- Live music.
- Food and beverage available for purchase

Belvorrow Sports Center, Maplecrest Falls
908-555-3162
www.belvorrowgrounds.example

Must include our logo (does not have to be huge) and County seal (both attached)

Colors

Designer to choose colors to be used in the design.

Requirements
Must have
• Should be fun and colorful
• The following info and attached logos:
• Rock, Paper, Scissors Championship - $$$ prizes
• Date: June 9th, 2018
• Time: 11am-4pm
• Fee: $2 to enter, free for spectators
• Heats to determine the overall ‘Rock, Paper, Scissors’ champion!
• - Cash prizes on offer
• - Live music.
• - Food and beverage available for purchase
• Belvorrow Sports Center, Maplecrest Falls
• 908-555-3162
• www.belvorrowgrounds.example
Nice to have
• There are a few inspirational photos attached to give an idea of what we are looking for.

```html
<!DOCTYPE html>
<html lang="en">
<head>
<meta charset="utf-8">
<title>Rock, Paper, Scissors Championship</title>
<link rel="stylesheet" href="https://fonts.googleapis.com/css2?family=Lilita+One&family=Merriweather:wght@700;900&display=swap">
<style>
  :root {
    --backdrop: #6e6266;
    --navy: #0f3d6b;
    --navy-text: #163f6e;
    --lime: #8cc63f;
    --lime-light: #b5e06a;
    --forest: #1d7f34;
    --white: #ffffff;
    --grey-text: #4a4a4a;
    --photo-top: #d8c7a4;
    --photo-mid: #a88f6a;
    --photo-low: #7f8fa6;
  }
  * { margin: 0; padding: 0; box-sizing: border-box; }
  html, body { width: 782px; height: 1200px; overflow: hidden; }
  body { background: var(--backdrop); position: relative; }

  .flyer {
    position: absolute; left: 21px; top: 77px;
    width: 740px; height: 1046px;
    background: var(--white);
    overflow: hidden;
    box-shadow: 0 10px 30px rgba(0,0,0,.35);
  }
  .hero-photo {
    position: absolute; left: 0; top: 0; width: 740px; height: 480px;
    background: linear-gradient(180deg, var(--photo-top) 0%, #c9b28a 35%, var(--photo-mid) 65%, var(--photo-low) 100%);
  }
  .navy-panel { position: absolute; left: 0; top: 0; width: 740px; height: 825px; }

  .county-seal {
    position: absolute; left: 584px; top: 23px; width: 144px; height: 144px;
    border-radius: 50%; background: var(--white);
    display: flex; align-items: center; justify-content: center; text-align: center;
    font-family: "Merriweather", serif; font-weight: 700; font-size: 19px; line-height: 1.2;
    color: var(--navy-text);
  }

  .headline {
    position: absolute; left: 0; top: 528px; width: 740px; text-align: center;
    font-family: "Lilita One", sans-serif; font-size: 58px; line-height: 62px;
    letter-spacing: 1px; text-transform: uppercase;
    color: var(--lime);
    background: linear-gradient(180deg, var(--lime-light), var(--lime) 60%, #6fae2a);
    -webkit-background-clip: text; background-clip: text; -webkit-text-fill-color: transparent;
  }
  .when {
    position: absolute; left: 0; top: 668px; width: 740px; text-align: center;
    font-family: "Merriweather", serif; font-weight: 700; font-size: 37px; line-height: 48px;
    color: var(--white); white-space: nowrap;
  }
  .fee-pill {
    position: absolute; left: 77px; top: 732px; width: 584px; height: 46px;
    border: 2px solid var(--white); border-radius: 14px;
    display: flex; align-items: center; justify-content: center;
    font-family: "Merriweather", serif; font-weight: 700; font-size: 26px;
    color: var(--white); text-transform: uppercase; white-space: nowrap;
    box-shadow: 0 8px 10px -6px rgba(0,0,0,.5);
  }
  .fee-pill .fee { color: var(--lime); margin-right: 8px; }

  .perks {
    position: absolute; left: 0; top: 843px; width: 740px; text-align: center;
    font-family: "Merriweather", serif; font-weight: 700; font-size: 28px; line-height: 35px;
    color: var(--navy-text); white-space: nowrap;
  }
  .call-to-action {
    position: absolute; left: 0; top: 920px; width: 740px; text-align: center;
    font-family: "Merriweather", serif; font-weight: 900; font-size: 29px; line-height: 38px;
    color: var(--forest);
  }
  .contact-band {
    position: absolute; left: 0; top: 960px; width: 740px; height: 46px;
    background: var(--lime);
    display: flex; align-items: center; justify-content: center;
    font-family: "Merriweather", serif; font-weight: 700; font-size: 24px; color: var(--white);
    white-space: nowrap;
  }
  .venue {
    position: absolute; left: 0; top: 1010px; width: 740px; text-align: center;
    font-family: "Merriweather", serif; font-weight: 700; font-size: 20px; line-height: 26px;
    color: var(--grey-text);
  }
</style>
</head>
<body>
  <main class="flyer">
    <div class="hero-photo" role="img" aria-label="Photo of five children on a beige sofa playing rock, paper, scissors in front of curtains"></div>

    <svg class="navy-panel" viewBox="0 0 740 825" aria-hidden="true">
      <path fill="#0f3d6b" d="M0 395 L18 400 L30 388 L44 402 L60 396 L75 420 L90 412 L110 440 L128 432 L150 452 L172 446 L196 462 L220 455 L246 470 L270 462 L300 476 L326 466 L352 480 L380 470 L410 478 L436 466 L462 476 L490 462 L516 470 L540 456 L566 462 L590 446 L612 452 L636 432 L660 438 L684 418 L706 422 L724 404 L740 408 L740 825 L0 825 Z"/>
    </svg>

    <div class="county-seal">Alder<br>County</div>

    <h1 class="headline">Rock, Paper, Scissors<br>Championship</h1>
    <p class="when">June 9th, 2018 Time: 11am-4pm</p>
    <p class="fee-pill"><span class="fee">$2 to enter,</span> free for spectators</p>

    <p class="perks">Cash prizes on offer | Live music.<br>Food and beverage available for purchase</p>
    <p class="call-to-action">CONTACT US TODAY</p>
    <p class="contact-band">908-555-3162 | www.belvorrowgrounds.example</p>
    <p class="venue">Belvorrow Sports Center, Maplecrest Falls</p>
  </main>
</body>
</html>
```